Harlow Grading and Septic needs a flyer to submit to contractors to offer our services

I need a sleek profession one page full color high gloss document showcasing our services to give to Mobile Home Companies and contractors that need our services.

Home Builders. Mobile Home Salesmen. People Building new homes.

Construction

Serif
Sans Serif

• Phone Number. Email address. Logo. Services offered: Mobile Home Pads, Meter Pole Placement and Connection, Waterline Connection, On Site Septic System Installs
• Jokes, Nothing trying to be cute

```html
<!DOCTYPE html>
<html lang="en">
<head>
<meta charset="utf-8">
<title>Harlow Grading and Septic – Contractor Flyer</title>
<link href="https://fonts.googleapis.com/css2?family=Oswald:wght@300;400;600;700&display=swap" rel="stylesheet">
<style>
  :root{
    --page:#ffffff;
    --sheet:#ddebf7;
    --brand-blue:#12508f;
    --brand-red:#d42027;
    --ink:#232323;
    --white:#ffffff;
    --soil:#a9734a;
    --sky:#6f9ccf;
  }
  *{box-sizing:border-box;margin:0;padding:0}
  html,body{width:1200px;height:1000px;overflow:hidden;background:var(--page);font-family:'Oswald',sans-serif}
  .flyer{position:absolute;left:341px;top:134px;width:518px;height:733px;background:var(--sheet)}
  .brand{position:absolute;left:31px;top:62px;width:227px;display:flex;align-items:center;gap:8px}
  .brand-mark{width:14px;height:14px;background:var(--brand-blue);flex:none}
  .brand-name{font-weight:700;font-size:21px;line-height:1.05;color:var(--brand-blue);text-transform:uppercase}
  .counties{position:absolute;left:340px;top:31px;width:148px;display:flex;flex-direction:column;gap:4px}
  .county-row{display:flex;gap:3px}
  .county{flex:1 1 auto;background:var(--brand-blue);color:var(--white);font-size:10.5px;line-height:14px;text-align:center;padding:0 3px;white-space:nowrap}
  .contact{position:absolute;left:340px;top:90px;width:160px}
  .contact-phone{display:flex;align-items:center;gap:6px;color:var(--brand-red);font-size:13px;font-style:italic;font-weight:400}
  .contact-line{display:flex;align-items:center;gap:5px;color:var(--ink);font-size:8.3px;font-weight:300;font-style:italic;margin-top:5px;margin-left:2px}
  .photo{position:absolute;border-radius:0}
  .photo.dig{left:31px;top:179px;width:147px;height:197px;background:linear-gradient(180deg,#4f6b3a 0%,#a9734a 35%,#b98457 100%)}
  .photo.pad{left:186px;top:179px;width:147px;height:110px;background:linear-gradient(180deg,#b7a78b 0%,#a65a37 55%,#9c4f30 100%)}
  .photo.spray{left:341px;top:179px;width:147px;height:197px;background:linear-gradient(180deg,#8aa8cc 0%,#b7b4a4 35%,#6e5440 100%)}
  .photo.tank-lift{left:31px;top:383px;width:147px;height:110px;background:linear-gradient(180deg,#1c5aa8 0%,#6f9ccf 55%,#5f7d3c 100%)}
  .photo.home-set{left:186px;top:296px;width:147px;height:197px;background:linear-gradient(180deg,#4f7fc0 0%,#cfd8e3 40%,#a88e6c 100%)}
  .photo.tank-set{left:341px;top:383px;width:147px;height:110px;background:linear-gradient(180deg,#4d7fc0 0%,#7d8c55 30%,#d0a57a 100%)}
  .headline{position:absolute;left:31px;top:514px;font-weight:700;font-size:39px;line-height:47px;color:var(--ink);letter-spacing:-0.3px}
  .headline .accent-blue{color:var(--brand-blue)}
  .headline .accent-red{color:var(--brand-red)}
  .region-band{position:absolute;left:31px;top:669px;width:219px;height:30px;background:var(--brand-blue);color:var(--white);font-size:16.5px;line-height:30px;text-align:center;font-weight:400}
  .services{position:absolute;left:267px;top:521px;width:230px}
  .service{margin-bottom:9px}
  .service-title{color:var(--brand-blue);font-size:16px;font-weight:400;line-height:20px;white-space:nowrap}
  .service-desc{color:var(--ink);font-size:9.6px;font-weight:300;font-style:italic;line-height:12.5px}
  .service.meter{margin-bottom:13px}
  .service.water{margin-bottom:11px}
</style>
</head>
<body>
<main class="flyer">
  <div class="brand">
    <span class="brand-mark"></span>
    <span class="brand-name">Harlow Grading<br>and Septic</span>
  </div>

  <div class="counties">
    <div class="county-row"><span class="county">Ellis</span><span class="county">Anderson</span><span class="county">Navarro</span></div>
    <div class="county-row"><span class="county">Henderson</span><span class="county">Kaufman</span><span class="county">Van Zandt</span></div>
    <div class="county-row"><span class="county">Smith</span><span class="county">Cherokee</span><span class="county">Limestone</span></div>
  </div>

  <div class="contact">
    <div class="contact-phone">
      <svg width="13" height="13" viewBox="0 0 24 24"><path fill="#12508f" d="M6.6 10.8a15.1 15.1 0 0 0 6.6 6.6l2.2-2.2c.3-.3.7-.4 1-.2 1.1.4 2.3.6 3.6.6.6 0 1 .4 1 1V20c0 .6-.4 1-1 1A17 17 0 0 1 3 4c0-.6.4-1 1-1h3.5c.6 0 1 .4 1 1 0 1.3.2 2.5.6 3.6.1.3 0 .7-.2 1z"/></svg>
      (555) 214-0736
    </div>
    <div class="contact-line">
      <svg width="8" height="6" viewBox="0 0 16 12"><rect width="16" height="12" fill="#12508f"/><path d="M0 0l8 6 8-6" stroke="#ddebf7" stroke-width="1.6" fill="none"/></svg>
      office@harlowgradingandseptic.com
    </div>
    <div class="contact-line">
      <svg width="7" height="7" viewBox="0 0 10 10"><circle cx="5" cy="5" r="5" fill="#12508f"/></svg>
      harlowgradingandseptic.com
    </div>
  </div>

  <div class="photo dig" role="img" aria-label="Excavator digging a septic trench beside a mobile home"></div>
  <div class="photo pad" role="img" aria-label="Finished septic field with lids in front of a mobile home"></div>
  <div class="photo spray" role="img" aria-label="Aerobic septic sprinkler spraying over graded soil"></div>
  <div class="photo tank-lift" role="img" aria-label="Concrete septic tank lifted by truck crane"></div>
  <div class="photo home-set" role="img" aria-label="Mobile home set on a graded pad with septic lids"></div>
  <div class="photo tank-set" role="img" aria-label="Excavator beside a newly installed septic tank"></div>

  <h1 class="headline"><span class="accent-blue">Expert</span> Mobile<br>Home Services<br>You Can <span class="accent-red">Trust</span></h1>

  <div class="region-band">Excavating Services in East Texas</div>

  <section class="services">
    <div class="service">
      <h2 class="service-title">Mobile Home Pads</h2>
      <p class="service-desc">Durable and stable pad installations for mobile homes.</p>
    </div>
    <div class="service meter">
      <h2 class="service-title">Meter Pole Placement and Connection</h2>
      <p class="service-desc">Professional meter pole placement and reliable<br>electrical connections.</p>
    </div>
    <div class="service water">
      <h2 class="service-title">Waterline Connection</h2>
      <p class="service-desc">Efficient and secure waterline connections for new homes.</p>
    </div>
    <div class="service">
      <h2 class="service-title">On Site Septic System Installs</h2>
      <p class="service-desc">Comprehensive septic system installations for your property.</p>
    </div>
  </section>
</main>
</body>
</html>
```